Business Card Design

Electronic Security Installation Specialists

Check out our website at www.brightpulsellc.com to see what we do.

Industry/Entity Type

Business

Contact Information for Business Card

Bright Pulse
Marianne Tolbert
218 Orchard Bend
Shepherdstow, WV 25443

Colors
3176b5
0455a3
ffffff

```html
<!DOCTYPE html>
<html lang="en">
<head>
<meta charset="utf-8">
<title>Bright Pulse – Business Card</title>
<link rel="stylesheet" href="https://fonts.googleapis.com/css2?family=Mulish:wght@300;400;600&display=swap">
<style>
  :root {
    --backdrop: #d9dadc;
    --brand-blue: #0455a3;
    --brand-blue-light: #3176b5;
    --front-top: #0f58a8;
    --front-bottom: #1a3f85;
    --ink-navy: #1b3a7a;
    --rule-light: #5d8fd0;
    --paper: #ffffff;
    --art-tone: #e7edf6;
  }
  * { box-sizing: border-box; margin: 0; padding: 0; }
  html, body { width: 1200px; height: 1200px; overflow: hidden; }
  body {
    background: var(--backdrop);
    font-family: "Mulish", "Helvetica Neue", Arial, sans-serif;
    position: relative;
  }
  .card { position: absolute; left: 276px; width: 636px; height: 402px; }

  /* Front */
  .card-front {
    top: 150px;
    background: linear-gradient(180deg, var(--front-top) 0%, var(--front-bottom) 100%);
    color: var(--paper);
  }
  .front-mark {
    position: absolute; left: 213px; top: 87px;
    width: 210px; height: 210px; border-radius: 50%;
    border: 4px solid var(--paper);
    background: #1d4488;
    display: flex; align-items: center; justify-content: center;
  }
  .front-mark .brand-name {
    font-size: 30px; font-weight: 400; letter-spacing: 0.5px; color: var(--paper);
  }
  .front-tagline {
    position: absolute; left: 0; right: 0; top: 352px;
    display: flex; align-items: center; gap: 12px;
    font-size: 17px; font-weight: 300;
  }
  .front-tagline::before, .front-tagline::after {
    content: ""; flex: 1; height: 1px; background: var(--rule-light);
  }

  /* Back */
  .card-back { top: 624px; background: var(--paper); color: var(--ink-navy); }
  .back-badge {
    position: absolute; left: 48px; top: 54px;
    width: 72px; height: 72px; border-radius: 50%;
    background: var(--brand-blue);
  }
  .back-brand { position: absolute; left: 138px; top: 58px; }
  .back-brand .brand-name {
    font-size: 33px; font-weight: 400; letter-spacing: 0.5px;
    text-transform: uppercase; line-height: 1; color: var(--ink-navy);
  }
  .back-brand .tagline { font-size: 14px; font-weight: 400; margin-top: 6px; color: var(--brand-blue-light); }
  .holder-name {
    position: absolute; left: 48px; top: 216px;
    font-size: 26px; font-weight: 400;
  }
  .cable-art {
    position: absolute; left: 0; top: 264px; width: 222px; height: 96px;
    background: linear-gradient(100deg, var(--paper) 0%, var(--art-tone) 100%);
  }
  .contact-list { position: absolute; left: 410px; top: 228px; list-style: none; }
  .contact-item {
    display: flex; align-items: flex-start; gap: 8px;
    font-size: 13px; line-height: 16px; margin-bottom: 13px;
    white-space: nowrap;
  }
  .contact-item svg { width: 22px; height: 22px; flex: none; fill: var(--ink-navy); }
</style>
</head>
<body>
  <section class="card card-front">
    <div class="front-mark"><span class="brand-name">Bright Pulse</span></div>
    <p class="front-tagline">Security Installation Specialists</p>
  </section>

  <section class="card card-back">
    <div class="back-badge"></div>
    <div class="back-brand">
      <p class="brand-name">Bright Pulse</p>
      <p class="tagline">Security Installation Specialists</p>
    </div>

    <h1 class="holder-name">Marianne Tolbert</h1>
    <div class="cable-art" role="img" aria-label="Line drawing of a coaxial cable end with connector"></div>

    <ul class="contact-list">
      <li class="contact-item">
        <svg viewBox="0 0 24 24" aria-hidden="true"><path d="M12 3 1.5 12H5v9h5v-6h4v6h5v-9h3.5z"/></svg>
        <span>218 Orchard Bend<br>Maple Falls, OR 97321</span>
      </li>
      <li class="contact-item">
        <svg viewBox="0 0 24 24" aria-hidden="true"><path d="M6.6 10.8a15.1 15.1 0 0 0 6.6 6.6l2.2-2.2a1 1 0 0 1 1-.25 11.4 11.4 0 0 0 3.6.57 1 1 0 0 1 1 1V20a1 1 0 0 1-1 1A17 17 0 0 1 3 4a1 1 0 0 1 1-1h3.5a1 1 0 0 1 1 1c0 1.25.2 2.45.57 3.57a1 1 0 0 1-.25 1z"/></svg>
        <span>T. 304 555 0142<br>M. 304 555 0187</span>
      </li>
      <li class="contact-item">
        <svg viewBox="0 0 24 24" aria-hidden="true"><path d="M12 2a10 10 0 1 0 0 20 10 10 0 0 0 0-20zm6.9 6h-2.9a15.7 15.7 0 0 0-1.4-3.6A8 8 0 0 1 18.9 8zM12 4a14 14 0 0 1 1.9 4h-3.8A14 14 0 0 1 12 4zM4.3 14a8 8 0 0 1 0-4h3.4a16.5 16.5 0 0 0 0 4zm.8 2H8a15.7 15.7 0 0 0 1.4 3.6A8 8 0 0 1 5.1 16zM8 8H5.1a8 8 0 0 1 4.3-3.6A15.7 15.7 0 0 0 8 8zm4 12a14 14 0 0 1-1.9-4h3.8A14 14 0 0 1 12 20zm2.3-6H9.7a14.7 14.7 0 0 1 0-4h4.6a14.7 14.7 0 0 1 0 4zm.3 5.6A15.7 15.7 0 0 0 16 16h2.9a8 8 0 0 1-4.3 3.6zM16.3 14a16.5 16.5 0 0 0 0-4h3.4a8 8 0 0 1 0 4z"/></svg>
        <span>www.brightpulsellc.com</span>
      </li>
      <li class="contact-item">
        <svg viewBox="0 0 24 24" aria-hidden="true"><path d="M2 5h20v14H2zm2 2v.5l8 5.5 8-5.5V7zm0 2.9V17h16V9.9l-8 5.5z"/></svg>
        <span>marianne@brightpulsellc.com</span>
      </li>
    </ul>
  </section>
</body>
</html>
```